Saving Lives with Dental Sleep Medicine

Looking for a brochure to market Dental Sleep Medicine educational courses . Whoever wins this bid will be hired to design the rest of our marketing campaign.
Design should be clean, simple with a modern feel. Not busy. Our courses utilize the most modern technology available.
Brochure content is attached, if you can't fit it all that is ok, we can tweak the content later. We are more focused on the look and feel of this design.
This brochure is marketing a 2 day course so there needs to be a spot for date, location, time & cost. As well as a notice of where to register VelmoraLearning.com, info@velmoralearning.com or call 1.800.###.#### and registration fees.
Also need a spot for Dr. Pelloquist's bio (attached). It's too long so just leave as much space as you can and we can amend the content.
Thank you so much. Looking forward to your designs. VelmEd Team :-)
Updates
Hello,
We are hoping for a minimalist design. Not busy. Clean and simple. We can reduce and minimize verbiage as needed. Just looking for layout and design.
Target Market(s)
Dentists
Requirements
Must have
- Clean lines, simple feel, minimalist and modern. Same font as logo. Black, white, gray.
Should not have
- Busy look and feel

```html
<!DOCTYPE html>
<html lang="en">
<head>
<meta charset="utf-8">
<title>Sleep &amp; Airway Management Brochure</title>
<link href="https://fonts.googleapis.com/css2?family=Montserrat:wght@300;400;500;600;700;800&family=Open+Sans:wght@400;600&display=swap" rel="stylesheet">
<style>
:root{
  --pink:#e96b7b;
  --pink-soft:#f08a96;
  --gray:#a3a2a8;
  --gray-dark:#8d8c93;
  --ink:#2a2a2c;
  --text:#3b3b3e;
  --paper:#ffffff;
  --bg:#e8e3e0;
}
*{box-sizing:border-box;margin:0;padding:0}
html,body{width:800px;height:1200px;overflow:hidden;background:var(--bg)}
body{font-family:"Montserrat",sans-serif;color:var(--text);position:relative}
.spread{position:absolute;left:20px;width:760px;height:537px;display:flex;box-shadow:0 6px 18px rgba(0,0,0,.18)}
.spread--covers{top:28px}
.spread--inside{top:630px}
.page{position:relative;width:380px;height:537px;background:var(--paper);overflow:hidden}
.photo{position:absolute}
.wordmark{display:flex;align-items:center;gap:6px;font-family:"Montserrat",sans-serif;font-weight:300;letter-spacing:.5px}
.wordmark__dot{width:12px;height:12px;background:var(--pink)}
/* back cover */
.bio-photo{left:26px;top:34px;width:100px;height:96px;background:linear-gradient(160deg,#d8d8dc,#6d6a74)}
.bio{position:absolute;font-family:"Open Sans",sans-serif;font-size:6.4px;line-height:1.42;text-align:justify;color:var(--text)}
.bio--intro{left:136px;top:34px;width:220px}
.bio--main{left:26px;top:140px;width:330px}
.bio--main p{margin-bottom:6px}
.back-shapes{position:absolute;left:0;top:0}
.fee-badge{position:absolute;left:245px;top:300px;width:92px;height:92px;border-radius:50%;background:var(--gray);color:#2a2a2c;display:flex;flex-direction:column;align-items:center;justify-content:center;font-weight:800;text-align:center;box-shadow:0 2px 4px rgba(0,0,0,.2)}
.fee-badge__label{font-size:8.5px;line-height:1.1}
.fee-badge__price{font-size:20px;margin-top:2px}
.contact{position:absolute;right:18px;bottom:36px;color:#fff;font-size:8px;text-align:right;line-height:2.2}
.contact li{list-style:none;display:flex;justify-content:flex-end;align-items:center;gap:6px}
.contact svg{flex:none}
.back-logo{position:absolute;left:38px;bottom:42px;color:#fff;font-size:15px}
.back-logo .wordmark__dot{background:#fff}
/* front cover */
.spine{position:absolute;left:0;top:0;width:16px;height:100%;background:var(--pink)}
.front-logo{position:absolute;left:0;right:0;top:26px;justify-content:center;color:var(--gray-dark);font-size:19px}
.hero{position:absolute;left:58px;top:62px}
.title{position:absolute;left:16px;right:0;top:318px;text-align:center;font-weight:800;text-transform:uppercase}
.title__top{color:var(--pink);font-size:18px;letter-spacing:.2px}
.title__bottom{color:var(--ink);font-size:21px;margin-top:2px}
.title__rule{width:70px;height:2px;background:var(--pink);margin:5px auto 0}
.subtitle{position:absolute;left:16px;right:0;top:383px;text-align:center;font-size:7.5px;color:#6a6a70;letter-spacing:.3px}
.field{position:absolute;display:flex;height:18px}
.field__label{background:var(--gray);color:#fff;font-size:9px;font-weight:600;padding:0 10px;display:flex;align-items:center;text-transform:uppercase}
.field__line{flex:1;border:1px solid #77767c;border-left:none}
.field--time{left:200px;top:402px;width:160px}
.field--date{left:40px;top:424px;width:200px}
.field--location{left:40px;top:446px;width:320px}
/* inside */
.col-photo{left:0;top:0;width:140px;height:537px;background:linear-gradient(180deg,#d9d6d2 0%,#7a5a44 35%,#3b3130 60%,#c7c2be 100%)}
.copy{position:absolute;left:152px;top:26px;width:212px}
.section-title{color:var(--pink);font-size:10.5px;font-weight:600;text-transform:uppercase;letter-spacing:.4px;border-bottom:1px solid var(--pink);display:inline-block;margin-bottom:7px}
.ticks{list-style:none}
.ticks li{position:relative;padding-left:12px;font-size:7px;line-height:1.3;margin-bottom:2.6px;color:var(--text)}
.ticks li::before{content:"";position:absolute;left:0;top:1px;width:7px;height:7px;border-radius:50%;background:var(--pink)}
.ticks li::after{content:"";position:absolute;left:2px;top:2.6px;width:3px;height:1.6px;border-left:1px solid #fff;border-bottom:1px solid #fff;transform:rotate(-45deg)}
.description{font-family:"Open Sans",sans-serif;font-size:6.6px;line-height:1.45;text-align:justify;margin-bottom:6px}
.section-title--desc{margin-top:10px}
.objectives{position:absolute;left:14px;top:26px;width:196px}
.objectives .ticks li{margin-bottom:7px}
.ph-a{left:228px;top:0;width:152px;height:150px;background:linear-gradient(160deg,#e6e2de,#5d5964)}
.ph-b{left:228px;top:154px;width:152px;height:170px;background:linear-gradient(200deg,#b8d2e6,#3f5567)}
.ph-c{left:0;top:328px;width:124px;height:104px;background:linear-gradient(180deg,#e2ded9,#6b4c3a)}
.ph-d{left:0;top:436px;width:124px;height:101px;background:linear-gradient(180deg,#3a4f6a,#c9b6a8)}
.ph-e{left:128px;top:328px;width:252px;height:209px;background:linear-gradient(180deg,#d7d3cf,#5a4a44 60%,#2f2d33)}
</style>
</head>
<body>

<section class="spread spread--covers">
  <div class="page page--back">
    <div class="photo bio-photo" role="img" aria-label="Portrait of Dr. Pelloquist in a suit, gesturing while speaking"></div>
    <p class="bio bio--intro">Dr. Pelloquist received his Doctor of Dental Surgery (DDS) Degree and Bachelor of Medical Sciences from Northfield University. He also earned fellowships from the Corvane Society of Restorative Dentistry and the Lakemont Institute for Advanced Dental Studies. He then furthered his education and training by completing a Research Fellowship in Dental Sleep Medicine at Harbourview University Hospital.</p>
    <div class="bio bio--main">
      <p>Dr. Pelloquist is a general dentist who maintains a group of private practices in Westbrook and Ridgefield with an interest in Dental Sleep Medicine and TMD Management. He is actively involved in clinical research in Dental Sleep Medicine and his research focuses on developing new technologies to improve treatment outcome predictability and patient selection in Oral Appliance Therapy for patients with OSA, utilizing different digital technologies and improving clinical workflow efficiencies. He is the recipient of several Clinical Excellence and Clinical Research Awards, and he has lectured at numerous meetings and many more Sleep meetings across North America and Europe.</p>
      <p>He is the founder and director of the Prairie Dental Sleep Study Club and the Clinical Director at the Quiet Night Centre. He is also the Chief Dental Officer at Nordvale Sleep Technologies, the developer of AirMap Plus technology. Dr. Pelloquist is a major advocate for the importance of an inter-disciplinary approach to Dental Sleep Medicine which focuses on the collaboration of sleep physicians, sleep dentists and other healthcare professionals. He has been treating OSA patients for many years and also has trained hundreds of dentists in Dental Sleep Medicine.</p>
    </div>
    <svg class="back-shapes" width="380" height="537" viewBox="0 0 380 537" aria-hidden="true">
      <path d="M0 418 Q120 450 245 455 L170 537 L0 537 Z" fill="var(--gray)"/>
      <path d="M380 300 L380 537 L150 537 Z" fill="var(--pink)"/>
    </svg>
    <div class="fee-badge">
      <span class="fee-badge__label">REGISTRATION<br>FEES</span>
      <span class="fee-badge__price">$XX</span>
    </div>
    <ul class="contact">
      <li>1.800.###.####
        <svg width="10" height="10" viewBox="0 0 10 10"><rect x="2.5" y="1" width="5" height="8" rx="1" fill="none" stroke="#fff" stroke-width="1"/></svg></li>
      <li>info@velmoralearning.com
        <svg width="10" height="10" viewBox="0 0 10 10"><rect x="1" y="2.5" width="8" height="5.5" fill="none" stroke="#fff" stroke-width="1"/><path d="M1 2.5 L5 6 L9 2.5" fill="none" stroke="#fff" stroke-width="1"/></svg></li>
      <li>www.VelmoraLearning.com
        <svg width="10" height="10" viewBox="0 0 10 10"><circle cx="5" cy="5" r="4" fill="none" stroke="#fff" stroke-width="1"/><path d="M1 5 H9 M5 1 V9" stroke="#fff" stroke-width=".8"/></svg></li>
    </ul>
    <div class="wordmark back-logo"><span class="wordmark__dot"></span>VelmoraLearning</div>
  </div>

  <div class="page page--front">
    <div class="spine"></div>
    <div class="wordmark front-logo"><span class="wordmark__dot"></span>VelmoraLearning</div>
    <svg class="hero" width="270" height="240" viewBox="0 0 270 240">
      <defs>
        <linearGradient id="heroFill" x1="0" y1="0" x2="0" y2="1">
          <stop offset="0" stop-color="#d9d5d1"/>
          <stop offset=".55" stop-color="#8a7d74"/>
          <stop offset="1" stop-color="#4a4248"/>
        </linearGradient>
      </defs>
      <polyline points="6,70 6,60 72,10 198,10" fill="none" stroke="var(--gray)" stroke-width="6"/>
      <polygon points="75,22 195,22 250,120 195,218 75,218 20,120" fill="none" stroke="var(--pink)" stroke-width="6"/>
      <polygon points="84,34 186,34 236,120 186,206 84,206 34,120" fill="url(#heroFill)" role="img" aria-label="Photo of a classroom lecture with dentists seated at tables and a presenter at a screen"/>
      <polyline points="264,170 264,180 198,230 72,230" fill="none" stroke="var(--gray)" stroke-width="6"/>
    </svg>
    <div class="title">
      <div class="title__top">Sleep &amp; Airway Management</div>
      <div class="title__bottom">In a Dental Clinic</div>
      <div class="title__rule"></div>
    </div>
    <p class="subtitle">AirMap Plus System &amp; Fully Digital Workflows for OAT</p>
    <div class="field field--time"><span class="field__label">Time</span><span class="field__line"></span></div>
    <div class="field field--date"><span class="field__label">Date</span><span class="field__line"></span></div>
    <div class="field field--location"><span class="field__label">Location</span><span class="field__line"></span></div>
  </div>
</section>

<section class="spread spread--inside">
  <div class="page page--inside-left">
    <div class="photo col-photo" role="img" aria-label="Photos of the hands-on clinical workshop with attendees filming a demonstration"></div>
    <div class="copy">
      <h2 class="section-title">Topics Covered:</h2>
      <ul class="ticks">
        <li>Fundamentals of Sleep &amp; Sleep Disorders</li>
        <li>Understand Obstructive Sleep Apnea (OSA) &amp; Treatment Options</li>
        <li>How to implement an effective Sleep Screening Protocol in a Dental Clinic</li>
        <li>Sleep Testing</li>
        <li>How to order an appliance for OAT</li>
        <li>Appliance Selection</li>
        <li>Importance of patient selection</li>
        <li>Overview of AirMap Plus System</li>
        <li>Hands-on workshop for AirMap Tray Fitting</li>
        <li>Hands-on workshop for Bite-Registration</li>
        <li>Technology &amp; Sleep</li>
        <li>Fully Digital Workflow for OAT</li>
        <li>AirMap Plus Case Studies</li>
        <li>Medical Billing for OAT</li>
        <li>How to maximize the utilization of your AirMap Plus at your clinic</li>
        <li>Simple and easy to follow clinical workflow</li>
      </ul>
      <h2 class="section-title section-title--desc">Course Description:</h2>
      <p class="description">Dental Sleep Medicine (DSM) has been growing rapidly over the past decade. Despite such growth, Oral Appliance Therapy (OAT) could be challenging in terms of predictability and workflow efficiency, resulting in many clinicians being reluctant to incorporate “Sleep &amp; OAT” into their clinics. However, most of these challenges can now be addressed by utilizing available technologies in healthcare industry, resulting in improved and predictable clinical workflows, patient experience, quality of care and access to care.</p>
      <p class="description">This program will review the importance of Sleep &amp; Airway Management in comprehensive inter-disciplinary treatment planning and how airway &amp; sleep disorders, if left untreated, could adversely impact the long-term prognosis of dental treatments. It will also provide a practical step-by-step guide for implementing a simple &amp; predictable “Sleep and Airway Management” program; utilizing easy to implement systems, improved patient communication &amp; education through intraoral scanning, &amp; 3D imaging AND a fully digital workflow for OAT.</p>
    </div>
  </div>

  <div class="page page--inside-right">
    <div class="objectives">
      <h2 class="section-title">Learning Objectives:</h2>
      <ul class="ticks">
        <li>Step by step instruction on how to systematically integrate sleep into your practice</li>
        <li>Why dental clinics should have a comprehensive understanding of sleep &amp; airway disorders, and educate their patients</li>
        <li>How to implement a sleep and airway management program in a dental clinic</li>
        <li>Overview of some of the latest technologies in dentistry and how each could be utilized in Dental Sleep Medicine (DSM)</li>
        <li>How to utilize your AirMap Plus System effectively in your clinic</li>
        <li>Proper selection of oral appliances for OSA</li>
        <li>Medical Billing for OAT</li>
      </ul>
    </div>
    <div class="photo ph-a" role="img" aria-label="Photo of the instructor presenting to seated attendees"></div>
    <div class="photo ph-b" role="img" aria-label="Photo of a monitor showing a 3D dental scan"></div>
    <div class="photo ph-c" role="img" aria-label="Photo of attendees gathered around a clinical demonstration"></div>
    <div class="photo ph-d" role="img" aria-label="Photo of a screen displaying an airway image"></div>
    <div class="photo ph-e" role="img" aria-label="Photo of the instructor leading a hands-on session in a dental operatory"></div>
  </div>
</section>

</body>
</html>
```